Labeling for Organic Food

we need a label design for

1. Organic Red Rice
2. Organic wild honey

it is going to be the same design in different dimensions.

1. Organic Red Rice
Dimension 1 28*18.5cm
Dimension 2 13.5*8cm

2. Organic Honey
12*6cm
Updates

Project Deadline Extended Reason: I still haven't found the right design. Added Monday, June 26, 2017

There is an update in the brief about using the Bhutanese color scheme. Please check it out.

Target Market(s)

people with the concern of health and the environment.

Requirements
Must have
• 1. our logo
• 2. All the info
• 3. A natural feel
• 4. I would prefer minimalistic style
• 5. Please include Bhutanese national colours as attached.

```html
<!DOCTYPE html>
<html lang="en">
<head>
<meta charset="utf-8">
<title>Verdanta Organic Red Rice Label</title>
<link rel="stylesheet" href="https://fonts.googleapis.com/css2?family=Comfortaa:wght@400;700&display=swap">
<style>
  :root {
    --frame-yellow: #ffd147;
    --paper: #ffffff;
    --royal-purple: #4e3b72;
    --pattern-magenta: #9b3f93;
    --ink: #1a1a1a;
  }
  * { box-sizing: border-box; margin: 0; padding: 0; }
  html, body {
    width: 1200px;
    height: 713px;
    overflow: hidden;
    background: var(--frame-yellow);
  }
  .label {
    position: relative;
    width: 1200px;
    height: 713px;
    background: var(--frame-yellow);
    font-family: "Comfortaa", sans-serif;
    color: var(--ink);
  }
  .label__panel {
    position: absolute;
    left: 27px;
    top: 22px;
    width: 1143px;
    height: 664px;
    background: var(--paper);
  }
  .brand {
    position: absolute;
    top: 62px;
    left: 0;
    width: 1200px;
    text-align: center;
    font-size: 58px;
    font-weight: 700;
    color: var(--ink);
    letter-spacing: 1px;
  }
  .product-title {
    position: absolute;
    top: 168px;
    left: 0;
    width: 1200px;
    text-align: center;
    font-size: 92px;
    font-weight: 400;
    color: var(--royal-purple);
    letter-spacing: 2px;
    line-height: 1;
  }
  .description {
    position: absolute;
    top: 307px;
    left: 0;
    width: 1200px;
    text-align: center;
    font-size: 19.5px;
    line-height: 27px;
  }
  .facts {
    position: absolute;
    top: 431px;
    left: 0;
    width: 1200px;
    text-align: center;
    font-size: 19.5px;
    line-height: 28px;
  }
  .facts strong { font-weight: 700; }
  .pattern-band {
    position: absolute;
    left: 0;
    top: 500px;
    width: 1200px;
    height: 93px;
    background: linear-gradient(90deg, var(--royal-purple), var(--pattern-magenta) 50%, var(--royal-purple));
  }
  .footer {
    position: absolute;
    top: 616px;
    font-size: 19.5px;
    line-height: 31px;
  }
  .footer--left { left: 60px; }
  .footer--center { left: 0; width: 1200px; text-align: center; font-weight: 700; }
  .footer--right { right: 51px; }
</style>
</head>
<body>
  <main class="label">
    <div class="label__panel"></div>

    <div class="brand">Verdanta</div>
    <h1 class="product-title">Organic Red Rice</h1>

    <p class="description">
      This organic red rice is 100% sourced from families farming around<br>
      the remote unpolluted lands in the Himalayans in Bhutan.<br>
      Chemical preservatives free, gluten free, mineeral rich, Organic Red Rice<br>
      is the healthiest choice for you and your loved ones.
    </p>

    <p class="facts">
      <strong>Ingredients:</strong> Organic Bhutanese Red Rice<br>
      <strong>Net Weight:</strong> 500g
    </p>

    <div class="pattern-band" role="img" aria-label="Band of nested purple and magenta diamond shapes in a traditional Bhutanese pattern"></div>

    <p class="footer footer--left">Best before 31/12/19<br>Product of Bhutan</p>
    <p class="footer footer--center">Distributed by Verdanta<br>27 Fernwood Lane Singapore 608812</p>
    <p class="footer footer--right">Store in a cool<br>and dry place</p>
  </main>
</body>
</html>
```